Brochure flyer for handout and web distribution - 11 X 17 folded four pages 8.5 X 11

We need a brochure for trade shows. Title page is "When Speed To Market Counts - We Deliver"- company logos on bottom of the page.

We build cannabis grow facilities and can build 3-6 months faster than conventional building methods. We want to use green as a focus color. We have an image cannabis interactive that we want to have in the center fold. It comes from this webpage which has the building descriptions - https://www.velmorak.com/cannabis-buildings

Also attached is an ad from Trivelex we did for a previous show that shows how I would like logos on the back cover - without the background image and without the text - replace text on back page with file attached with key advantages that we would like on the back page as well.

There are also some images from our partner BralloDeck that we would love to show on the inside cover as well - so one page is Velmor interactive and buildings and the other inside page features BralloDeck.

For content on Brallo-Deck - When choosing between modular construction and traditionally constructed rooms, consider that all modular construction is objectively faster and more affordable. On average you can cut construction time by half when using a modular room and building design compared to conventionally construction. All components used to construct modular rooms and buildings have already been designed and fabricated at our plant, causing:
• Less disruption to your daily business operations
• Less construction waste and debris
Logos are attached for the back page - these can also be used on the front page. Website is www.hollenfarbuildworks.com (visit us). Contact us at info@hollenfarbuildworks.com

All images can be provided EPS - final design will need to be 300DPI minimum

Target Market(s)

Lead investors in Cannabis

Industry/Entity Type

Cannabis Industry

Font styles to use
Serif

Colors
0094D4
00A9DD
6FCCEA
C7EBF8
E9F6FB
00AB8E
00BBA5
67D7C9
C6EFE9
E9F9F6

Requirements
Must have
• Logos, website, 4 pages
Should not have
• Cannabis images

```html
<!DOCTYPE html>
<html lang="en">
<head>
<meta charset="utf-8">
<title>When Speed To Market Counts - Brochure</title>
<link rel="stylesheet" href="https://fonts.googleapis.com/css2?family=Oswald:wght@500;600&family=Roboto+Condensed:wght@400;700&display=swap">
<style>
:root{
  --stage:#e6e6e6;
  --ink:#0b0b0b;
  --paper:#ffffff;
  --red:#d62b2b;
  --purple:#6b3f9c;
  --teal:#1aa88e;
  --teal-text:#12977f;
  --orange:#e8462c;
  --label-red:#e0453a;
  --body:#444;
  --chip:#d9d9d9;
  --leaf-dark:#0f2a12;
  --leaf-mid:#2f6b2c;
}
*{box-sizing:border-box;margin:0;padding:0}
html,body{width:741px;height:1200px;overflow:hidden;background:var(--stage)}
body{position:relative;font-family:"Roboto Condensed",Arial,sans-serif;color:var(--body)}
.spread{position:absolute;display:flex;box-shadow:0 6px 14px rgba(0,0,0,.18)}
.page{position:relative;overflow:hidden}
.page--dark{background:var(--ink);color:#ddd}
.page--light{background:var(--paper)}

/* outer spread */
.spread--outer{left:67px;top:40px;width:602px;height:370px}
.spread--outer .page{width:301px;height:370px}
.partner-row{position:absolute;left:26px;top:146px;display:flex;gap:14px}
.partner{width:53px;height:53px;border-radius:50%;background:var(--chip);display:flex;align-items:center;justify-content:center;text-align:center;font-size:6.5px;font-weight:700;color:#222;line-height:1.1;padding:4px}
.back-copy{position:absolute;left:40px;top:225px;width:222px;text-align:center;font-size:5px;line-height:1.5;color:#cfcfcf}
.back-copy ul{list-style:none;margin-top:6px}
.contact-band{position:absolute;left:0;top:329px;width:100%;height:20px;display:flex;align-items:center;gap:8px;padding-left:20px;font-size:6px;color:#fff;white-space:nowrap}
.contact-band b{font-weight:700}
.contact-band--back{background:linear-gradient(90deg,var(--purple),var(--red))}
.contact-band--front{background:linear-gradient(90deg,var(--red),var(--purple))}
.cover-photo{position:absolute;inset:0;background:radial-gradient(circle at 60% 40%,var(--leaf-mid),var(--leaf-dark) 70%)}
.cover-title{position:absolute;left:20px;top:92px;width:270px;font-family:"Oswald",sans-serif;font-weight:600;color:#fff;font-size:24px;line-height:1;letter-spacing:.3px;white-space:nowrap}
.cover-tag{position:absolute;left:50px;top:123px;width:200px;height:32px;background:var(--red);border-radius:5px;display:flex;align-items:center;justify-content:center;font-family:"Oswald",sans-serif;font-weight:600;color:#fff;font-size:20px;white-space:nowrap}
.cover-logos{position:absolute;left:65px;top:242px;display:flex;gap:5px}
.logo-tile{height:64px;background:rgba(240,240,240,.92);border-radius:4px;display:flex;align-items:center;justify-content:center;font-size:9px;font-weight:700;color:#222;text-align:center;padding:4px}

/* inner spread */
.spread--inner{left:67px;top:535px;width:602px;height:364px}
.spread--inner .page{width:301px;height:364px}
.section-head{position:absolute;height:18px;border-radius:4px;color:#fff;font-size:10.5px;display:flex;align-items:center;justify-content:center;white-space:nowrap}
.section-head--teal{left:20px;top:25px;width:260px;background:var(--teal)}
.section-head--orange{left:18px;top:138px;width:262px;background:var(--orange)}
.intro{position:absolute;font-size:5.5px;line-height:1.4}
.intro--teal{left:22px;top:52px;width:255px;color:var(--teal-text)}
.benefits{position:absolute;left:22px;top:80px;width:175px;list-style:none}
.benefits li{font-size:5.5px;line-height:1.4;margin-bottom:17.5px}
.benefits b{color:var(--teal-text)}
.benefits b.alt{color:var(--label-red)}
.product{position:absolute;left:205px;width:80px;background:linear-gradient(160deg,#f1f1f1,#b9b9b9)}
.aerial{position:absolute;left:0;top:0;width:301px;height:140px;background:linear-gradient(180deg,#cfd6d4,#9fae8e)}
.intro--plain{left:22px;top:164px;width:262px;color:#555}
.buildings{position:absolute;left:22px;top:198px;width:262px;display:grid;grid-template-columns:1fr 1fr;column-gap:12px;list-style:none}
.buildings li{font-size:5px;line-height:1.35;margin-bottom:9px;color:#666}
.buildings b{display:block;font-size:5.5px;color:var(--label-red)}
.num{display:inline-block;width:7px;height:7px;border-radius:50%;background:var(--label-red);color:#fff;font-size:5px;text-align:center;line-height:7px;margin-right:2px}
.email-line{position:absolute;left:66px;top:340px;width:170px;display:flex;align-items:center;gap:4px;color:var(--label-red);font-size:8.5px;white-space:nowrap}
.email-line span{flex:1;height:1px;background:var(--label-red)}

/* thumbnails */
.thumb{position:absolute;top:986px;width:297px;height:149px;display:flex;box-shadow:0 4px 8px rgba(0,0,0,.18)}
.thumb .page{width:50%;height:100%}
.thumb--outer{left:63px}
.thumb--inner{left:381px}
.t-chips{position:absolute;left:12px;top:58px;display:flex;gap:6px}
.t-chips i{width:26px;height:26px;border-radius:50%;background:var(--chip)}
.t-copy{position:absolute;left:16px;top:92px;width:118px;text-align:center;font-size:4px;color:#ccc}
.t-band{position:absolute;left:0;top:134px;width:100%;height:7px;font-size:2.8px;color:#fff;padding-left:8px;line-height:7px;white-space:nowrap}
.t-title{position:absolute;left:10px;top:38px;font-family:"Oswald",sans-serif;font-weight:600;color:#fff;font-size:10px;white-space:nowrap}
.t-tag{position:absolute;left:25px;top:52px;width:98px;height:13px;background:var(--red);border-radius:3px;font-family:"Oswald",sans-serif;font-weight:600;color:#fff;font-size:8.5px;text-align:center;line-height:13px;white-space:nowrap}
.t-logos{position:absolute;left:32px;top:98px;display:flex;gap:3px}
.t-logos i{height:26px;background:rgba(240,240,240,.92);border-radius:2px}
.t-head{position:absolute;height:8px;border-radius:2px;color:#fff;font-size:4.4px;line-height:8px;text-align:center;white-space:nowrap}
.t-text{position:absolute;font-size:4px;line-height:1.4;color:#666}
</style>
</head>
<body>

<section class="spread spread--outer" aria-label="Back and front cover">
  <article class="page page--dark back-cover">
    <div class="partner-row">
      <div class="partner">Kestrin Enterprises</div>
      <div class="partner">Brallo-Deck</div>
      <div class="partner">DRAVIKSHOP.COM</div>
      <div class="partner">Velmor</div>
    </div>
    <div class="back-copy">
      <p>For content on Brallo-Deck - When choosing between modular construction and traditionally constructed rooms, consider that all modular constructio is objectively faster and more affordable. On average you can cut construction time by half when using a modular room and building design compared to conventionally construction. All components used to construct modular rooms and buildings have already been designed and fabricated at our plant, causing:</p>
      <ul><li>• Less disruption to your daily business operations</li><li>• Less construction waste and debris</li></ul>
    </div>
    <div class="contact-band contact-band--back"><span><b>VISIT US:-</b> www.hollenfarbuildworks.com</span><span><b>CONTACT US:-</b> info@hollenfarbuildworks.com</span></div>
  </article>
  <article class="page page--dark front-cover">
    <div class="cover-photo" role="img" aria-label="Dark green foliage photograph filling the cover"></div>
    <h1 class="cover-title">WHEN SPEED TO MARKET</h1>
    <div class="cover-tag">COUNTS - WE DELIVER</div>
    <div class="cover-logos">
      <div class="logo-tile" style="width:71px">Kestrin Enterprises</div>
      <div class="logo-tile" style="width:96px">Velmor</div>
    </div>
    <div class="contact-band contact-band--front"><span><b>VISIT US:-</b> www.hollenfarbuildworks.com</span><span><b>CONTACT US:-</b> info@hollenfarbuildworks.com</span></div>
  </article>
</section>

<section class="spread spread--inner" aria-label="Inside spread">
  <article class="page page--light">
    <h2 class="section-head section-head--teal">CRAFT GROWTH MODEL ADVANTAGES AND BENEFITS</h2>
    <p class="intro intro--teal">Our cultivators enjoy several distinct advantages and benefits compared to conventional steel building orpol ycarbonate/glass greenhouse construction:</p>
    <ul class="benefits">
      <li><b>Build Faster:-</b> At least 12 weeks faster than conventional construction of the exterior and interior structureaccelerating time to first harvest</li>
      <li><b>Built Better:-</b> Deliver a fully engineered, code complaint, expandable and relocatable facility using our team of designers, manufacturers, and installers</li>
      <li><b>Superior Grow Environment:-</b> Full blackout-controlled environmentanchored by high-performance LED lights(PPF efficacy 2.85 µmols/J)</li>
      <li><b>Airtight Facility:-</b> A sealed, airtight building solution critical for energy efficiency, maintaining CO2 levels and providing enhanced biosecurity</li>
      <li><b class="alt">Reduced Energy Use:-</b> Tensioned membrane structure uses less energy than traditional structure, with electricity usage being consistent throughout facilit</li>
      <li><b>Increased Profits:-</b> Speed to market can generate almost $2.1 million in additional crop revenue, plus beat your licensee competitors to market</li>
      <li><b>Financing:-</b> Qualified growers can receive interim and long term financing from non-traditional sources for certain components of our integrated solution</li>
      <li><b>Committed Team:-</b> Experienced vendor-partner team engaged in the process from beginning to end to assure your facility is completed and operational in a timely manner</li>
    </ul>
    <div class="product" style="top:66px;height:40px" role="img" aria-label="Modular room panel product photo"></div>
    <div class="product" style="top:114px;height:36px" role="img" aria-label="Modular room exterior product photo"></div>
    <div class="product" style="top:162px;height:52px" role="img" aria-label="Lit grow room interior photo"></div>
    <div class="product" style="top:240px;height:94px;background:linear-gradient(160deg,#7d8c78,#3d4a3a)" role="img" aria-label="Vertical racking system photo"></div>
  </article>
  <article class="page page--light">
    <div class="aerial" role="img" aria-label="Aerial illustration of a campus of numbered membrane buildings"></div>
    <h2 class="section-head section-head--orange">IMMEDIATE BUILDINGS FOR CANNABIS PRODUCTION</h2>
    <p class="intro intro--plain">Velmor structures are the ideal solution for growers, processors and producers of cannabis products. Our versatile structures are engineered to be built virtually anywhere and are perfect for on-site processing. Designed to be relocatable Velmor structures can be moved and repurposed as needs change, adapting to growth in your industry.</p>
    <ul class="buildings">
      <li><b><span class="num">1</span>Blackout Growing Structures</b>Complete control over your growing environment in a large clearspan structure.</li>
      <li><b><span class="num">5</span>Processing Facilities</b>Eliminate the need to transport crops to off-site processing facilities, eliminating damage. Velmor's clear-span design provides space for the personnel and machinery used to dry, extract, manufacture and package your products.</li>
      <li><b><span class="num">2</span>Greenhouse Growing Structures</b>Velmor's specially designed, highly translucent membrane provides diffused lighting for optimal growing conditions and backed by a 10 year membrane guarantee.</li>
      <li><b><span class="num">6</span>Administration Buildings</b>Bright spacious buildings with large windows and daylight panels provide a comfortable space for your on-site admin team.</li>
      <li><b><span class="num">3</span>On-site Composting</b>Avoid pests, mold and rain by composting in a Velmor Structure</li>
      <li><b><span class="num">7</span>Retail</b>Provide your customers with a welcoming retail experience either on site or in convenient urban locations.</li>
      <li><b><span class="num">4</span>Head houses</b>Give your staff space to prepare and protect your crops during the growing process.</li>
      <li><b><span class="num">8</span>Hail Shelters</b>Protect millions of dollars in crops with hail shelters</li>
    </ul>
    <div class="email-line"><span></span>info@velmor.com<span></span></div>
  </article>
</section>

<section class="thumb thumb--outer" aria-label="Cover spread preview">
  <div class="page page--dark">
    <div class="t-chips"><i></i><i></i><i></i><i></i></div>
    <p class="t-copy">Modular rooms cut build time in half.</p>
    <div class="t-band contact-band--back">www.hollenfarbuildworks.com</div>
  </div>
  <div class="page page--dark">
    <div class="cover-photo" role="img" aria-label="Dark green foliage photograph"></div>
    <div class="t-title">WHEN SPEED TO MARKET</div>
    <div class="t-tag">COUNTS - WE DELIVER</div>
    <div class="t-logos"><i style="width:34px"></i><i style="width:46px"></i></div>
    <div class="t-band contact-band--front">info@hollenfarbuildworks.com</div>
  </div>
</section>

<section class="thumb thumb--inner" aria-label="Inside spread preview">
  <div class="page page--light">
    <div class="t-head" style="left:8px;top:12px;width:130px;background:var(--teal)">CRAFT GROWTH MODEL ADVANTAGES AND BENEFITS</div>
    <p class="t-text" style="left:10px;top:26px;width:90px">Faster builds, better results.</p>
    <div class="product" style="left:104px;top:30px;width:36px;height:100px" role="img" aria-label="Product photos column"></div>
  </div>
  <div class="page page--light">
    <div class="aerial" style="width:100%;height:58px" role="img" aria-label="Aerial building campus illustration"></div>
    <div class="t-head" style="left:10px;top:57px;width:128px;background:var(--orange)">IMMEDIATE BUILDINGS FOR CANNABIS PRODUCTION</div>
    <p class="t-text" style="left:12px;top:72px;width:124px">Velmor buildings for every stage.</p>
    <p class="t-text" style="left:40px;top:140px;color:var(--label-red)">info@velmor.com</p>
  </div>
</section>

</body>
</html>
```